Brightfield Steel Depot (Metal Roofing Manufacturing and Supply) needs a billboard design

We need a billboard design for for our metal roofing manufacturing company in Sarasota FL, Brightfield Steel Depot Inc. You can visit our website www.brightfieldsteeldepot-example.com for more info about our company. We located are off Exit 210 on I 75- 482 Harrowgate Rd. Sarasota 34290
The billboard will be on I75 north of our office

I have a design that I am interested in but waiting on minor corrections from designer

```html
<!DOCTYPE html>
<html lang="en">
<head>
<meta charset="utf-8">
<title>Brightfield Steel Depot – Billboard</title>
<link href="https://fonts.googleapis.com/css2?family=Montserrat:wght@500;600;700;800;900&display=swap" rel="stylesheet">
<style>
  :root {
    --canvas-bg: #eeeff1;
    --photo-dark: #3a3f44;
    --photo-mid: #5b6160;
    --photo-warm: #6d6a58;
    --panel-violet: rgba(112, 102, 150, 0.62);
    --logo-white: #ffffff;
    --brand-blue: #1f4fa0;
    --brand-yellow: #f2d22e;
    --headline-yellow: #f1e83c;
    --text-white: #ffffff;
  }
  * { box-sizing: border-box; margin: 0; padding: 0; }
  html, body {
    width: 1200px;
    height: 1179px;
    overflow: hidden;
    background: var(--canvas-bg);
    font-family: "Montserrat", sans-serif;
  }
  .billboard {
    position: absolute;
    left: 40px;
    top: 426px;
    width: 1120px;
    height: 327px;
    overflow: hidden;
    box-shadow: 4px 5px 8px rgba(0, 0, 0, 0.35);
  }
  .house-photo {
    position: absolute;
    inset: 0;
    background:
      linear-gradient(180deg, rgba(40, 44, 48, 0.55) 0%, rgba(40, 44, 48, 0) 35%),
      linear-gradient(100deg, var(--photo-dark) 0%, var(--photo-mid) 45%, var(--photo-warm) 70%, var(--photo-dark) 100%);
  }
  .brand-box {
    position: absolute;
    left: 53px;
    top: 0;
    width: 360px;
    height: 133px;
    background: var(--logo-white);
    display: flex;
    align-items: center;
    padding-left: 36px;
    gap: 10px;
  }
  .brand-mark {
    width: 16px;
    height: 16px;
    border-radius: 50%;
    background: var(--brand-yellow);
    flex: none;
  }
  .brand-name {
    color: var(--brand-blue);
    font-weight: 600;
    font-size: 23px;
    letter-spacing: -0.2px;
    white-space: nowrap;
  }
  .contact-panel {
    position: absolute;
    left: 53px;
    top: 133px;
    width: 360px;
    height: 194px;
    background: var(--panel-violet);
    color: var(--text-white);
    padding: 86px 0 0 18px;
  }
  .contact-cta {
    font-weight: 800;
    font-size: 25px;
    line-height: 1;
    letter-spacing: 0.2px;
  }
  .contact-phone {
    font-weight: 800;
    font-size: 45px;
    line-height: 1;
    margin-top: 8px;
    letter-spacing: 0.5px;
  }
  .headline {
    position: absolute;
    right: 43px;
    top: 100px;
    text-align: right;
    color: var(--headline-yellow);
    line-height: 1;
    white-space: nowrap;
  }
  .headline-top {
    display: block;
    font-weight: 600;
    font-size: 47px;
    letter-spacing: 1px;
  }
  .headline-main {
    display: block;
    font-weight: 900;
    font-size: 72px;
    margin-top: 6px;
    letter-spacing: -0.5px;
  }
  .headline-bottom {
    display: block;
    font-weight: 500;
    font-size: 61px;
    margin-top: 6px;
    letter-spacing: 0.5px;
  }
</style>
</head>
<body>
  <section class="billboard">
    <div class="house-photo" role="img" aria-label="Photo of a two-storey Florida home with a grey standing-seam metal roof, framed by palm trees"></div>

    <div class="brand-box">
      <span class="brand-mark"></span>
      <span class="brand-name">Brightfield Steel Depot</span>
    </div>

    <div class="contact-panel">
      <p class="contact-cta">Get your quote today!</p>
      <p class="contact-phone">941-555-0187</p>
    </div>

    <h1 class="headline">
      <span class="headline-top">FLORIDA'S PREMIER</span>
      <span class="headline-main">METAL ROOF</span>
      <span class="headline-bottom">MANUFACTURER</span>
    </h1>
  </section>
</body>
</html>
```